依頼詳細
https://www.hikarinova-ex.jp/pr/1/
こちらのLPサイトへ誘導バナーです。
現在、同時に制作中の為PC用のサイトしか用意しておりません。後日、スマホ用のサイトも完成予定です。
サイズは
横 240 × 縦 120 (表示 120 × 60)
横 936 × 縦 120 (表示 468 × 60)
横 468 × 縦 120 (表示 234 × 60)
横 600 × 縦 500 (表示 300 × 250)
横 200 × 縦 120 (表示 100 × 60)
横 640 × 縦 100 (表示 320 × 50)
横250 × 縦 250 (表示 125 × 125)
横200 × 縦 200 (表示 100 × 100)
容量制限
200KB 以下
ファイル形式:
JPG / PNG /
記載項目
電気まだ変えてないの?
サイト名:光ノバケアネット
特に細かく決めていないので、よいキャッチなどがありましたら作成して頂ければと思います。
サイズ
• 250 x 250 ( スクエアポップアップ )
• 200 x 200 ( スクエア )
• 240×120/936×120/468×120/600×500/200×120/640×100
希望イメージ
シンプル 複雑
単色 カラフル
暗い 明るい
日常 高級
遊び心 厳粛
未来的 伝統的
女性的 男性的
希望する色
黄・オレンジ系、緑系、水色系
納品ファイル
• 高解像度JPG (.jpg)
• PNG形式 (.png)
補足説明
■ 選んだ理由

修正にも素早いご対応をして頂きました。
バナーのデザインをお願いしたのですが、シンプルで程よい文字数だった為
選ばせて頂きました。

■ 提案者全員のお礼・コメント

今回、素早い対応をして頂きありがとうございました。
また、次回お願いすることもあると思いますので
その際は、よろしくお願いいたします。

```html
<!DOCTYPE html>
<html lang="ja">
<head>
<meta charset="utf-8">
<title>光ノバケアネット バナー</title>
<link rel="stylesheet" href="https://fonts.googleapis.com/css2?family=Noto+Sans+JP:wght@500;700;900&family=M+PLUS+Rounded+1c:wght@800&display=swap">
<style>
  :root {
    --green: #2f9a2a;
    --green-dark: #23801f;
    --green-text: #3c9a3a;
    --sky: #e6f3f7;
    --ink: #1c1c1c;
    --orange: #f08a1c;
    --orange-light: #ffc21a;
    --white: #ffffff;
    --bulb: #f7d84a;
    --tagline: #444444;
  }
  html, body {
    margin: 0;
    padding: 0;
    overflow: hidden;
    background: var(--white);
  }
  .banner {
    position: relative;
    width: 1200px;
    height: 600px;
    background: var(--sky);
    overflow: hidden;
    font-family: "Noto Sans JP", sans-serif;
  }
  .banner__ribbon {
    position: absolute;
    top: 0;
    left: 0;
    width: 1200px;
    height: 150px;
  }
  .banner__headline {
    position: absolute;
    top: 16px;
    left: 160px;
    margin: 0;
    font-size: 66px;
    font-weight: 700;
    color: var(--white);
    letter-spacing: 0.14em;
    line-height: 1.2;
    white-space: nowrap;
  }
  .banner__bulb {
    position: absolute;
    top: 62px;
    left: 1048px;
    width: 96px;
    height: 128px;
    border-radius: 50% 50% 30% 30%;
    background: radial-gradient(circle at 50% 35%, #fff2a0, var(--bulb) 60%, #d9b21e);
  }
  .banner__claim {
    position: absolute;
    left: 80px;
    top: 206px;
    margin: 0;
  }
  .banner__claim-lead {
    display: block;
    font-size: 82px;
    font-weight: 900;
    color: var(--ink);
    line-height: 1.1;
    letter-spacing: 0.02em;
  }
  .banner__claim-rate {
    display: block;
    margin-top: 6px;
    font-size: 106px;
    font-weight: 900;
    color: var(--orange);
    line-height: 1.1;
    letter-spacing: 0.14em;
  }
  .banner__figure {
    position: absolute;
    left: 560px;
    top: 150px;
    width: 560px;
    height: 330px;
  }
  .banner__brand {
    position: absolute;
    left: 80px;
    top: 474px;
  }
  .banner__brand-name {
    display: block;
    font-size: 44px;
    font-weight: 500;
    color: var(--green-text);
    line-height: 1.2;
    letter-spacing: 0.02em;
  }
  .banner__brand-tagline {
    display: block;
    margin-left: 96px;
    font-size: 13px;
    font-weight: 500;
    color: var(--tagline);
    letter-spacing: 0.28em;
  }
  .banner__cta {
    position: absolute;
    left: 756px;
    top: 492px;
    width: 412px;
    height: 84px;
    background: var(--green);
    border: 3px solid var(--green-dark);
    box-sizing: border-box;
    color: var(--white);
    font-size: 38px;
    font-weight: 700;
    display: flex;
    align-items: center;
    justify-content: center;
    gap: 18px;
    letter-spacing: 0.04em;
  }
  .banner__cta-arrow {
    width: 26px;
    height: 30px;
  }
</style>
</head>
<body>
<main class="banner">
  <svg class="banner__ribbon" viewBox="0 0 1200 150" aria-hidden="true">
    <polygon points="0,0 1200,0 1200,96 720,150 0,102" fill="var(--green)"/>
  </svg>
  <p class="banner__headline">電気まだ変えてないの?</p>
  <div class="banner__bulb" role="img" aria-label="光る電球のイラスト"></div>

  <h1 class="banner__claim">
    <span class="banner__claim-lead">電気代削減</span>
    <span class="banner__claim-rate">成功率</span>
  </h1>

  <svg class="banner__figure" viewBox="0 0 560 330" role="img" aria-label="92%">
    <defs>
      <linearGradient id="figureFill" x1="0" y1="0" x2="0" y2="1">
        <stop offset="0" stop-color="var(--orange-light)"/>
        <stop offset="1" stop-color="var(--orange)"/>
      </linearGradient>
    </defs>
    <text x="6" y="312" font-family="'M PLUS Rounded 1c', sans-serif" font-weight="800"
          fill="url(#figureFill)" stroke="var(--green)" stroke-width="16" stroke-linejoin="round"
          paint-order="stroke">
      <tspan font-size="370" letter-spacing="-26">92</tspan><tspan font-size="170" dx="4">%</tspan>
    </text>
  </svg>

  <div class="banner__brand">
    <span class="banner__brand-name">光ノバケアネット</span>
    <span class="banner__brand-tagline">暮らしの電気をもっと賢く</span>
  </div>

  <div class="banner__cta">
    詳細はコチラ
    <svg class="banner__cta-arrow" viewBox="0 0 26 30" aria-hidden="true">
      <polygon points="0,0 26,15 0,30" fill="var(--white)"/>
    </svg>
  </div>
</main>
</body>
</html>
```